braided hoses

Mr Colin Mayfair <colinmmayfair@quillnest.net>
Tue, Jun 25, 3:27 PM (17 hours ago)
to Priya

WE ARE LOOKING FOR A FLYER WE CAN EMAIL OU TO EXISTING CUSTOMERS - MECHANICAL INDUSTRIAL WHOLESALE ETC

WE SUPPLY PERFORMANCE FITTINGS TO MAKE BRAIDED HOSE FOR RACECAR, ENTHUSIASTS AND GENERAL CARS
these are used for
brake hoses
cooler lines
oil + fuel hoses

pictures supplied but if better pictures found will be ok
i do not want to pay for pictures afterwards

Requirements
Must have
• company details correct

```html
<!DOCTYPE html>
<html lang="en">
<head>
<meta charset="utf-8">
<title>Braided Hoses – Kestrel Auto Supply</title>
<link rel="stylesheet" href="https://fonts.googleapis.com/css2?family=Bebas+Neue&family=Poppins:wght@500;600;700&display=swap">
<style>
  :root {
    --yellow-top: #f9dc0c;
    --yellow-bottom: #f8a91b;
    --ink: #111111;
    --white: #ffffff;
    --shadow-grey: #8d8a8a;
    --hose-silver: #a7a6a2;
    --hose-dark: #4a4a48;
    --fitting-red: #c8232c;
    --fitting-blue: #2f55a8;
  }
  * { box-sizing: border-box; margin: 0; padding: 0; }
  html, body { width: 915px; height: 1200px; overflow: hidden; background: #e9e9e9; }
  .flyer {
    position: relative; width: 915px; height: 1200px; overflow: hidden;
    background: var(--white);
    font-family: "Poppins", sans-serif; color: var(--ink);
  }
  .backdrop { position: absolute; inset: 0; }
  .headline {
    position: absolute; left: 36px; top: 62px;
    font-family: "Bebas Neue", sans-serif; font-size: 98px; line-height: 84px;
    color: var(--white); -webkit-text-stroke: 2px var(--ink); letter-spacing: 0;
  }
  .brand {
    position: absolute; left: 600px; top: 196px; width: 310px; text-align: center;
    font-weight: 700; font-size: 20px; letter-spacing: 1px; color: var(--ink);
  }
  .brand-mark {
    display: block; width: 18px; height: 18px; border-radius: 50%;
    background: var(--ink); margin: 0 auto 8px;
  }
  .tagline {
    position: absolute; left: 36px; top: 252px;
    font-weight: 700; font-size: 23px; line-height: 31.5px; text-transform: uppercase;
  }
  .hose-photo {
    position: absolute; left: 470px; top: 360px; width: 445px; height: 380px;
    background: radial-gradient(ellipse at 60% 45%, var(--hose-silver) 0%, #c9c8c4 45%, rgba(255,255,255,0) 72%);
  }
  .section-bar {
    position: absolute; display: flex; align-items: center; justify-content: center;
    font-weight: 700; font-size: 23px; letter-spacing: 0.5px;
  }
  .section-bar::after {
    content: ""; position: absolute; left: 20px; right: 0; top: 100%; height: 18px;
    background: linear-gradient(to bottom, rgba(0,0,0,0.35), rgba(0,0,0,0));
    clip-path: polygon(0 0, 100% 0, 90% 100%, 10% 100%);
  }
  .contact-bar { left: 0; top: 604px; width: 375px; height: 53px; background: var(--white); }
  .uses-bar {
    left: 515px; top: 812px; width: 400px; height: 50px;
    background: linear-gradient(to right, var(--yellow-top), var(--yellow-bottom));
  }
  .contact-list { position: absolute; left: 36px; top: 690px; list-style: none; }
  .contact-list li {
    display: flex; align-items: flex-start; gap: 11px;
    font-weight: 600; font-size: 18.5px; line-height: 23px; margin-bottom: 13px;
  }
  .contact-icon {
    flex: 0 0 24px; width: 24px; height: 24px; border-radius: 50%;
    background: var(--white); display: flex; align-items: center; justify-content: center;
    margin-top: 1px;
  }
  .contact-icon svg { width: 14px; height: 14px; }
  .uses-list { position: absolute; left: 555px; top: 893px; list-style: none; }
  .uses-list li {
    display: flex; align-items: center; gap: 12px; height: 55px; margin-bottom: 11px;
    font-weight: 600; font-size: 19.5px;
  }
  .use-icon {
    width: 54px; height: 54px; border: 2.5px solid var(--ink); border-radius: 50%;
    display: flex; align-items: center; justify-content: center;
  }
  .use-icon svg { width: 28px; height: 28px; }
  .fitting-frame {
    position: absolute; left: 100px; top: 935px; width: 320px; height: 320px;
    border-radius: 50%; border: 12px solid var(--yellow-bottom); background: var(--white);
    box-shadow: inset 0 0 0 12px var(--white), inset 0 0 0 14px #dcdcdc;
  }
  .fitting-photo {
    position: absolute; left: 60px; top: 55px; width: 175px; height: 130px;
    border-radius: 40px 20px 40px 20px;
    background: linear-gradient(120deg, var(--fitting-red) 0%, var(--fitting-red) 45%, var(--fitting-blue) 60%, var(--fitting-blue) 100%);
  }
</style>
</head>
<body>
<main class="flyer">
  <svg class="backdrop" width="915" height="1200" viewBox="0 0 915 1200" aria-hidden="true">
    <defs>
      <linearGradient id="yellowFade" x1="0" y1="0" x2="0" y2="1">
        <stop offset="0" stop-color="var(--yellow-top)"/>
        <stop offset="1" stop-color="var(--yellow-bottom)"/>
      </linearGradient>
      <linearGradient id="curveShade" x1="0" y1="0" x2="1" y2="0">
        <stop offset="0" stop-color="#6f6c6c"/>
        <stop offset="1" stop-color="#d8d6d6"/>
      </linearGradient>
    </defs>
    <rect width="915" height="1200" fill="url(#yellowFade)"/>
    <path d="M915 275 C700 230 505 330 488 520 C475 700 440 930 300 1020 C220 1070 120 1075 0 1068 L0 1200 L915 1200 Z" fill="var(--white)"/>
    <path d="M915 298 C740 260 560 330 520 440 C600 350 760 330 915 355 Z" fill="url(#curveShade)" opacity="0.85"/>
    <path d="M503 600 C495 760 470 900 380 1000 C450 930 490 800 503 600 Z" fill="url(#curveShade)" opacity="0.6"/>
  </svg>

  <h1 class="headline">Braided<br>Hoses</h1>

  <div class="brand"><span class="brand-mark"></span>KESTREL AUTO SUPPLY</div>

  <p class="tagline">We supply performance<br>fittings to make<br>braided hose for<br>racecar,<br>enthusiasts<br>and general cars</p>

  <div class="hose-photo" role="img" aria-label="Photo of three stainless steel braided hoses"></div>

  <h2 class="section-bar contact-bar">CONTACT:</h2>

  <ul class="contact-list">
    <li><span class="contact-icon"><svg viewBox="0 0 16 16"><text x="8" y="12.5" text-anchor="middle" font-size="13" font-family="Poppins, sans-serif" fill="var(--yellow-bottom)">@</text></svg></span>parts@kestrelautosupply.co.nz</li>
    <li><span class="contact-icon"><svg viewBox="0 0 16 16"><path d="M4 1.5l2.5 3-1.5 1.5c.8 1.8 2.2 3.2 4 4l1.5-1.5 3 2.5-1.5 2.5C7 13.5 2.5 9 1.5 3z" fill="var(--yellow-bottom)"/></svg></span>0800 55 61 48</li>
    <li><span class="contact-icon"><svg viewBox="0 0 16 16"><path d="M8 1a5 5 0 0 0-5 5c0 3.5 5 9 5 9s5-5.5 5-9a5 5 0 0 0-5-5zm0 7a2 2 0 1 1 0-4 2 2 0 0 1 0 4z" fill="var(--yellow-bottom)"/></svg></span>27 Weaver St, Millbrook,<br>Hamilton</li>
    <li><span class="contact-icon"><svg viewBox="0 0 16 16" fill="none" stroke="var(--yellow-bottom)" stroke-width="1.2"><circle cx="8" cy="8" r="6.5"/><ellipse cx="8" cy="8" rx="3" ry="6.5"/><path d="M1.5 8h13M2.5 4.8h11M2.5 11.2h11"/></svg></span>kestrelautosupply.co.nz</li>
  </ul>

  <h2 class="section-bar uses-bar">USES</h2>

  <ul class="uses-list">
    <li><span class="use-icon"><svg viewBox="0 0 28 28"><path d="M6 12l2.5-6h11l2.5 6h1.5v7h-2v2h-3v-2h-9v2h-3v-2h-2v-7z" fill="var(--ink)"/><path d="M9.5 7.5h9l1.5 4h-12z" fill="var(--white)"/><circle cx="8.5" cy="15.5" r="1.5" fill="var(--white)"/><circle cx="19.5" cy="15.5" r="1.5" fill="var(--white)"/></svg></span>brake hoses</li>
    <li><span class="use-icon"><svg viewBox="0 0 28 28" fill="none" stroke="var(--ink)" stroke-width="1.6"><rect x="4" y="4" width="20" height="20" rx="1.5"/><circle cx="14" cy="14" r="7"/><circle cx="14" cy="14" r="1.5" fill="var(--ink)"/><path d="M14 7v14M7 14h14M9 9l10 10M19 9L9 19"/></svg></span>cooler lines</li>
    <li><span class="use-icon"><svg viewBox="0 0 28 28"><rect x="6" y="4" width="11" height="19" rx="1.5" fill="var(--ink)"/><rect x="8" y="6.5" width="7" height="5" fill="var(--white)"/><rect x="4.5" y="22" width="14" height="2.5" fill="var(--ink)"/><path d="M17 9h2.5l2 3v8a1.5 1.5 0 0 0 3 0V10l-2.5-3" fill="none" stroke="var(--ink)" stroke-width="1.5"/></svg></span>oil + fuel hoses</li>
  </ul>

  <div class="fitting-frame">
    <div class="fitting-photo" role="img" aria-label="Photo of a red and blue anodised 90 degree hose fitting"></div>
  </div>
</main>
</body>
</html>
```